Background of Our Business: TQB Financial Services provides accounting and tax services to small businesses. Website: www.tqbfsx.com.au. Our slogan is: one stop finance department service for small businesses.
I would like a flyer design with 2 sides.
1st side)
Business Logo; TQB - Finance Department Service for Small Businesses (Please refer file 1 as attached)

Large text of: Too many things going on? Smaller text: Let us reduce your input into accounts, you can focus on more value adding areas.

Our Services: Bookkeeping, Payroll, Financial Statement, Tax Advisory, Tax Return, Business Performance Measurement, Business Decision Support, Assistance in Loan Applications, and much more.

Why Us: Our clients are handpicked, we are fully committed to your business, and our works are performed at corporate standard. We utilise technology to save your accounting cost, monitor your compliance risks, provide solid data for business decision making, and be your representative in dealing with banks and NRB. (Please also refer file 2 as attached)

Contact details: Address: 58 Dunmore Street, Carlisle, WA 6101
PO Box 2493, East Victoria Park, WA 6981
Tel: (08) 6287 3914; Mob: 0491 738 226

2nd side)
Our Pricing: Charge by transaction volumes; Fixed fee advised beforehand. hourly rate please refer file 4 as attached.

Our 'Gold' level service subscriber receives:
Frequent bookkeeping, payroll, and financial reporting services
Integrate tax advisory, compliance risk monitoring and control
Free regular preliminary business performance check
Free assistance in commercial loan and mortgage application
Free hand picked business insights for your industry
Free representative service for you in dealing with banks, NRB.

Coupon Section: Sign up now and receive 10% off for your next 12 months bill. Valid until 31/07/2016.

```html
<!DOCTYPE html>
<html lang="en">
<head>
<meta charset="utf-8">
<title>TQB Financial Services – Two-Sided Flyer</title>
<link href="https://fonts.googleapis.com/css2?family=Open+Sans:ital,wght@0,300;0,400;0,600;0,700;1,400&family=Oswald:wght@300&family=Kaushan+Script&display=swap" rel="stylesheet">
<style>
:root{
  --cyan:#12abd6;
  --cyan-dark:#0a9bc4;
  --navy:#1d3a6e;
  --ink:#1c1c1c;
  --black:#0d0d0d;
  --grey-card:#e4e0dd;
  --stage:#efefef;
  --white:#ffffff;
}
*{box-sizing:border-box;margin:0;padding:0}
html,body{width:1200px;height:1200px;overflow:hidden}
body{background:var(--stage);font-family:"Open Sans",Arial,sans-serif;color:var(--ink);position:relative}
.page{position:absolute;top:148px;width:555px;height:786px;background:var(--white);overflow:hidden;box-shadow:0 10px 24px rgba(0,0,0,.18)}
.page--front{left:51px}
.page--back{left:621px}
.abs{position:absolute}

/* brand */
.brand{display:flex;flex-direction:column}
.brand__name{display:flex;align-items:center;gap:8px;font-weight:700;color:var(--navy);font-size:46px;line-height:1;letter-spacing:1px}
.brand__mark{width:30px;height:30px;background:var(--navy)}
.brand__rule{height:1px;background:var(--navy);margin:6px 0 3px;width:192px}
.brand__tag{font-size:7.6px;color:var(--navy);font-weight:600;letter-spacing:-.1px}

/* front */
.url-bar{left:337px;top:45px;width:190px;height:23px;background:var(--black);color:var(--white);font-size:13.5px;display:flex;align-items:center;justify-content:center;letter-spacing:.2px}
.hero{left:0;top:116px;width:555px;height:256px;background:linear-gradient(180deg,#dcdcdc 0%,#f4f4f4 55%,#ffffff 76%,#c9a77e 77%,#b48f63 92%,#f3f3f3 93%,#fff 100%)}
.hero__title{left:20px;top:218px;font-size:34px;line-height:40px;font-weight:700;color:var(--cyan);letter-spacing:-.3px;white-space:nowrap}
.hero__lead{left:20px;top:260px;font-size:17.5px;line-height:21px;color:var(--ink)}
.notch{left:264px;top:372px;width:0;height:0;border-left:18px solid transparent;border-right:18px solid transparent;border-top:16px solid #b48f63}
.benefit-title{left:0;top:404px;width:555px;text-align:center;font-size:16px;font-weight:700}
.benefit-rule{left:27px;width:500px;height:1px;background:#444}
.benefits{left:20px;top:447px;width:515px;display:flex}
.benefit{flex:1 1 0;text-align:center;font-size:11.2px;line-height:13px;border-left:1px solid #444;padding-top:6px;height:80px}
.benefit:first-child{border-left:none}
.benefit__icon{width:29px;height:29px;border-radius:50%;background:var(--cyan);margin:0 auto 13px;display:flex;align-items:center;justify-content:center}
.section-title{font-size:16px;font-weight:700;letter-spacing:.2px}
.why{left:19px;top:553px;width:276px}
.why p{margin-top:8px;font-size:11.6px;line-height:14.2px;text-align:justify;color:#222}
.services{left:322px;top:553px;width:225px}
.ticks{list-style:none;margin-top:8px}
.ticks li{position:relative;padding-left:14px;font-size:11.6px;line-height:14.2px;color:#222;white-space:nowrap}
.ticks li::before{content:"";position:absolute;left:0;top:2.5px;width:10px;height:10px;border-radius:50%;background:var(--cyan)}
.ticks li::after{content:"";position:absolute;left:3.3px;top:4.6px;width:3px;height:5px;border:solid var(--white);border-width:0 1.5px 1.5px 0;transform:rotate(45deg)}
.address{left:19px;top:717px;width:445px;font-size:11.3px;font-weight:600;letter-spacing:-.15px;white-space:nowrap}
.corner-square{left:475px;top:700px;width:60px;height:40px;background:var(--black)}
.footer{left:0;top:740px;width:555px;height:46px;background:var(--black);display:flex;align-items:center}
.footer__cta{position:absolute;left:0;top:0;height:46px;width:140px;background:var(--cyan);clip-path:polygon(0 0,100% 0,88% 100%,0 100%);font-size:12px;font-weight:700;color:var(--black);display:flex;align-items:center;padding-left:23px}
.footer__contact{position:absolute;left:151px;color:var(--white);font-size:11.8px;white-space:nowrap}
.footer__contact b{font-weight:700}

/* back */
.desk{left:0;top:0;width:555px;height:196px;background:linear-gradient(100deg,#efe2cc 0%,#eadbc2 50%,#d9c6a6 100%)}
.back-brand{left:26px;top:28px}
.slogan{left:26px;top:135px;font-size:13.8px;line-height:16px;font-weight:700;color:var(--navy)}
.pricing-title{left:26px;top:208px;font-size:16px;font-weight:700}
.pricing-lead{left:26px;top:238px;font-size:11.8px;white-space:nowrap}
.plan{border-radius:14px;padding:20px 8px 0;color:var(--white)}
.plan--bronze{left:14px;top:286px;width:174px;height:204px;background:var(--cyan)}
.plan--gold{left:189px;top:272px;width:176px;height:232px;background:var(--grey-card);color:#1a1a1a;padding-top:34px}
.plan--plat{left:366px;top:286px;width:174px;height:204px;background:var(--cyan)}
.plan__name{text-align:center;font-size:12.8px;font-weight:700;padding-bottom:8px;border-bottom:1.5px dashed currentColor}
.plan__rows{padding:6px 0 5px;border-bottom:1.5px dashed currentColor}
.plan__row{display:flex;justify-content:space-between;font-size:9.7px;line-height:12.7px;font-weight:300;white-space:nowrap}
.plan--gold .plan__row{font-weight:400}
.plan__note{font-size:8.2px;line-height:10.8px;font-weight:300;padding:7px 6px 0}
.plan--gold .plan__note{font-weight:400}
.gold-title{left:19px;top:518px;font-size:12.6px;font-weight:600}
.gold-list{left:19px;top:532px;width:390px}
.paper-stack{left:437px;top:508px;width:55px;height:144px;background:linear-gradient(90deg,#e2e2e2,#fafafa 50%,#d6d6d6)}
.offer{left:26px;top:664px;width:120px;text-align:center;line-height:1}
.offer__small{display:block;font-family:"Oswald",Arial,sans-serif;font-weight:300;font-size:38px;letter-spacing:.5px}
.offer__big{display:block;font-family:"Kaushan Script",cursive;font-size:46px;margin-top:-2px}
.offer-divider{left:168px;top:664px;height:96px;border-left:1px dashed #777}
.stripe{left:187px;width:338px;height:5px;background:var(--cyan)}
.coupon{left:187px;top:678px;width:338px;text-align:center}
.coupon__lead{font-size:17.5px;color:#333}
.coupon__deal{font-size:17.5px;font-weight:700;margin-top:1px}
.valid{left:187px;top:742px;width:338px;text-align:center;font-size:10.5px;font-style:italic;color:#444}
.back-bar{left:0;top:774px;width:555px;height:12px;background:var(--black)}
.back-bar::before{content:"";position:absolute;left:0;top:0;height:12px;width:136px;background:var(--cyan);clip-path:polygon(0 0,100% 0,96% 100%,0 100%)}
</style>
</head>
<body>

<!-- FRONT SIDE -->
<section class="page page--front">
  <div class="brand abs" style="left:19px;top:22px">
    <div class="brand__name"><span class="brand__mark"></span>TQB</div>
    <div class="brand__rule"></div>
    <div class="brand__tag">Finance Department Service for Small Businesses</div>
  </div>
  <div class="url-bar abs">www.tqbfsx.com.au</div>

  <div class="hero abs" role="img" aria-label="Bright office scene with a wall clock, a wooden desk, a printer and stacked papers"></div>
  <h1 class="hero__title abs">Too many things going on?</h1>
  <p class="hero__lead abs">Let us reduce your input into accounts,<br>you can focus on more value adding areas.</p>
  <div class="notch abs"></div>

  <h2 class="benefit-title abs">How do we BENEFIT your business?</h2>
  <div class="benefit-rule abs" style="top:438px"></div>
  <div class="benefits abs">
    <div class="benefit">
      <div class="benefit__icon"><svg width="14" height="14" viewBox="0 0 14 14"><rect x="2" y="1" width="10" height="12" fill="none" stroke="#fff" stroke-width="1.5"/><path d="M4 5h6M4 8h6M4 10.5h4" stroke="#fff" stroke-width="1.2"/></svg></div>
      We work<br>for you
    </div>
    <div class="benefit">
      <div class="benefit__icon"><svg width="14" height="14" viewBox="0 0 14 14"><rect x="1.5" y="1.5" width="11" height="11" rx="2" fill="none" stroke="#fff" stroke-width="1.5"/><path d="M4 7l2 2 4-4" fill="none" stroke="#fff" stroke-width="1.6"/></svg></div>
      at Corporate<br>Standard
    </div>
    <div class="benefit">
      <div class="benefit__icon"><svg width="15" height="14" viewBox="0 0 15 14"><circle cx="5" cy="8" r="3" fill="none" stroke="#fff" stroke-width="2" stroke-dasharray="2 1.2"/><circle cx="11" cy="4" r="2.2" fill="none" stroke="#fff" stroke-width="1.6" stroke-dasharray="1.5 1"/></svg></div>
      Utilise<br>Technology
    </div>
    <div class="benefit">
      <div class="benefit__icon"><svg width="14" height="14" viewBox="0 0 14 14"><path d="M3 12V8M6 12V4M9 12V6M2 12.5h10" stroke="#fff" stroke-width="2"/></svg></div>
      Provide<br>solid data
    </div>
    <div class="benefit" style="flex-grow:1.3">
      <div class="benefit__icon"><svg width="14" height="14" viewBox="0 0 14 14"><rect x="1.5" y="2.5" width="11" height="10" fill="none" stroke="#fff" stroke-width="1.4"/><path d="M1.5 5.5h11M4 1v3M10 1v3" stroke="#fff" stroke-width="1.4"/><rect x="5" y="7.5" width="4" height="3" fill="#fff"/></svg></div>
      Monitor<br>Compliance Risk
    </div>
    <div class="benefit" style="flex-grow:1.3">
      <div class="benefit__icon"><svg width="16" height="14" viewBox="0 0 16 14"><circle cx="8" cy="4" r="2.2" fill="#fff"/><circle cx="3.5" cy="5.5" r="1.7" fill="#fff"/><circle cx="12.5" cy="5.5" r="1.7" fill="#fff"/><path d="M4.5 13v-3.5a3.5 3.5 0 0 1 7 0V13zM0.5 12v-2.5a3 3 0 0 1 3.5-2.7M15.5 12v-2.5a3 3 0 0 0-3.5-2.7" fill="#fff"/></svg></div>
      Your Finance<br>Representative
    </div>
  </div>
  <div class="benefit-rule abs" style="top:534px"></div>

  <div class="why abs">
    <h3 class="section-title">WHY US?</h3>
    <p>Our clients are handpicked, we are fully committed to your business, and our works are performed at corporate standard. We utilise technology to save your accounting cost, monitor your compliance risks, provide solid data for business decision making, and be your representative in dealing with banks and NRB.</p>
  </div>
  <div class="services abs">
    <h3 class="section-title">OUR SERVICES:</h3>
    <ul class="ticks">
      <li>Bookkeeping &amp; Payroll</li>
      <li>Financial Statement</li>
      <li>Tax Advisory &amp; Tax Return</li>
      <li>Business Performance Measurement</li>
      <li>Business Decision Support</li>
      <li>Assistance in Loan Applications</li>
      <li>and much more.</li>
    </ul>
  </div>

  <p class="address abs">58 Dunmore Street, Carlisle, WA 6101 | PO Box 2493, East Victoria Park, WA 6981</p>
  <div class="corner-square abs"></div>
  <footer class="footer abs">
    <div class="footer__cta">SIGN UP NOW!</div>
    <p class="footer__contact"><b>Tel:</b> (08) 6287 3914 &nbsp;| &nbsp;<b>Mob:</b> &nbsp;0491 738 226 &nbsp;| &nbsp;<b>Mail:</b> hello@tqbfsx.com.au</p>
  </footer>
</section>

<!-- BACK SIDE -->
<section class="page page--back">
  <div class="desk abs" role="img" aria-label="Light wooden desk with a keyboard, mouse, cup of coffee, pencil and notepad"></div>
  <div class="brand back-brand abs">
    <div class="brand__name"><span class="brand__mark"></span>TQB</div>
    <div class="brand__rule"></div>
    <div class="brand__tag">Finance Department Service for Small Businesses</div>
  </div>
  <p class="slogan abs">One Stop Finance Department<br>Service for Small Businesses</p>

  <h2 class="pricing-title abs">PRICING?</h2>
  <p class="pricing-lead abs">We charge by transaction volumes, we have fixed fee advised beforehand and hourly rate.</p>

  <div class="plan plan--bronze abs">
    <div class="plan__name">BRONZE</div>
    <div class="plan__rows">
      <div class="plan__row"><span>Bookkeeping &amp; Payroll:</span><span>$50/hr</span></div>
      <div class="plan__row"><span>Taxation:</span><span>$110/hr</span></div>
      <div class="plan__row"><span>Management Accounting:</span><span>$110/hr</span></div>
      <div class="plan__row"><span>Finance:</span><span>POA, Generally Free</span></div>
      <div class="plan__row"><span>General Consulting:</span><span>Free*</span></div>
    </div>
    <p class="plan__note">*Free charge for consulting in general topics, without us have to go through large quantities of documents. Fees will be advised beforehand if there is any.</p>
  </div>
  <div class="plan plan--gold abs">
    <div class="plan__name">GOLD</div>
    <div class="plan__rows">
      <div class="plan__row"><span>Bookkeeping &amp; Payroll:</span><span>$45/hr</span></div>
      <div class="plan__row"><span>Taxation:</span><span>$99/hr</span></div>
      <div class="plan__row"><span>Management Accounting:</span><span>$99/hr</span></div>
      <div class="plan__row"><span>Finance:</span><span>POA, Generally Free</span></div>
      <div class="plan__row"><span>General Consulting:</span><span>Free*</span></div>
    </div>
    <p class="plan__note">*Free charge for consulting in general topics, without us have to go through large quantities of documents. Fees will be advised beforehand if there is any.</p>
  </div>
  <div class="plan plan--plat abs">
    <div class="plan__name">PLANTIUM</div>
    <div class="plan__rows">
      <div class="plan__row"><span>Bookkeeping &amp; Payroll:</span><span>$40/hr</span></div>
      <div class="plan__row"><span>Taxation:</span><span>$88/hr</span></div>
      <div class="plan__row"><span>Management Accounting:</span><span>$88/hr</span></div>
      <div class="plan__row"><span>Finance:</span><span>POA, Generally Free</span></div>
      <div class="plan__row"><span>General Consulting:</span><span>Free*</span></div>
    </div>
    <p class="plan__note">*Free charge for consulting in general topics, without us have to go through large quantities of documents. Fees will be advised beforehand if there is any.</p>
  </div>

  <h3 class="gold-title abs">Our ‘Gold’ level service subscriber receives:</h3>
  <ul class="ticks gold-list abs">
    <li>Frequent bookkeeping, payroll, and financial reporting services</li>
    <li>Integrate tax advisory, compliance risk monitoring and control</li>
    <li>Free regular preliminary business performance check</li>
    <li>Free assistance in commercial loan and mortgage application</li>
    <li>Free hand picked business insights for your industry</li>
    <li>Free representative service for you in dealing with banks, NRB.</li>
  </ul>
  <div class="paper-stack abs" role="img" aria-label="Tall stack of paper documents"></div>

  <div class="offer abs"><span class="offer__small">SPECIAL</span><span class="offer__big">Offer</span></div>
  <div class="offer-divider abs"></div>
  <div class="stripe abs" style="top:666px"></div>
  <div class="coupon abs">
    <p class="coupon__lead">Sign up now and receive</p>
    <p class="coupon__deal">10% off for your next 12 months bill.</p>
  </div>
  <div class="stripe abs" style="top:727px"></div>
  <p class="valid abs">This offer is valid until 31/07/2016.</p>
  <div class="back-bar abs"></div>
</section>

</body>
</html>
```